Animal Eye Clinic needs a Business card

We are a new veterinary ophthalmology practice (Tessaly Animal Eye Care) and we need a business card designed. We only see animal eyes - we are not a regular veterinary clinic. We already have a logo. We are looking for a professional, good looking business card to hand out to our clients. We are looking for something simple but professional and contemporary. Our logo is likely the only picture/graphic that needs to be on the card.
Updates

Contact Information for Business Card

Marisol Dunkley, BSc, DVM, MSc, DipACVO
Veterinary Ophthalmologist

Phone: 250.418.3097
Email: tessalyanimaleyecare@mailbrook.net
Website: tessalyanimaleyecare.net
Address: 1840 Pellworth Rd
Kelowna, BC, V4T 8M3

Colors

Designer to choose colors to be used in the design.

Requirements
Must have
• Our logo (attached)

```html
<!DOCTYPE html>
<html lang="en">
<head>
<meta charset="utf-8">
<title>Tessaly Animal Eye Care – Business Card</title>
<link href="https://fonts.googleapis.com/css2?family=Roboto:wght@300;400;500&display=swap" rel="stylesheet">
<style>
  :root {
    --teal: #1a9aa8;
    --ink: #5c5c5c;
    --soft: #8f8f8f;
    --paper: #ffffff;
    --backdrop: #9a9a9a;
    --backdrop-light: #c4c4c4;
  }
  * { box-sizing: border-box; margin: 0; padding: 0; }
  html, body { width: 1200px; height: 930px; overflow: hidden; }
  body {
    position: relative;
    background: radial-gradient(ellipse at 50% 45%, var(--backdrop-light), var(--backdrop) 75%);
    font-family: "Roboto", Arial, sans-serif;
  }
  .card {
    position: absolute;
    width: 520px;
    height: 300px;
    background: var(--paper);
    border-radius: 18px;
    box-shadow: 0 6px 18px rgba(0,0,0,0.22);
  }
  .card--front { left: 70px; top: 110px; }
  .card--back { left: 610px; top: 500px; }

  .front-brand {
    position: absolute;
    left: 0; right: 0; top: 0; bottom: 0;
    display: flex;
    align-items: center;
    justify-content: center;
    gap: 16px;
  }
  .brand-dot {
    width: 52px; height: 52px;
    border-radius: 50%;
    background: var(--teal);
  }
  .brand-name {
    color: var(--teal);
    font-weight: 500;
    font-size: 27px;
    letter-spacing: 0.3px;
  }

  .back-mark {
    position: absolute;
    left: 40px; top: 70px;
    width: 150px; height: 150px;
    border-radius: 50%;
    background: var(--teal);
  }
  .back-info {
    position: absolute;
    left: 225px; top: 42px;
    right: 20px;
  }
  .person-name {
    color: var(--teal);
    font-weight: 400;
    font-size: 30px;
    line-height: 1.1;
  }
  .credentials, .role {
    color: var(--soft);
    font-weight: 300;
    font-size: 13px;
    line-height: 1.4;
  }
  .credentials { margin-top: 4px; }
  .address {
    margin-top: 14px;
    color: var(--ink);
    font-weight: 300;
    font-size: 16px;
    line-height: 1.3;
  }
  .contacts { margin-top: 14px; list-style: none; }
  .contacts li {
    display: flex;
    align-items: center;
    gap: 9px;
    color: var(--ink);
    font-weight: 300;
    font-size: 14.5px;
    line-height: 1.45;
  }
  .contacts svg { width: 12px; height: 12px; flex: none; }
  .contacts .web strong { font-weight: 400; }
</style>
</head>
<body>
  <section class="card card--front">
    <div class="front-brand">
      <span class="brand-dot"></span>
      <span class="brand-name">Tessaly Animal Eye Care</span>
    </div>
  </section>

  <section class="card card--back">
    <div class="back-mark" role="img" aria-label="Tessaly Animal Eye Care brand mark area"></div>
    <div class="back-info">
      <h1 class="person-name">Marisol Dunkley</h1>
      <p class="credentials">BSc, DVM, MSc, DipACVO</p>
      <p class="role">Veterinary Ophthalmologist</p>
      <p class="address">Address: 1840 Pellworth Rd<br>Kelowna, BC, V4T 8M3</p>
      <ul class="contacts">
        <li>
          <svg viewBox="0 0 12 12" aria-hidden="true"><path d="M2.5 1 L4.5 1 L5.2 3.4 L3.9 4.4 Q5 6.9 7.6 8.1 L8.6 6.8 L11 7.5 L11 9.5 Q10.5 11 9 11 Q1 10 1 2.8 Q1 1.2 2.5 1 Z" fill="var(--teal)"/></svg>
          250.418.3097
        </li>
        <li>
          <svg viewBox="0 0 12 12" aria-hidden="true"><rect x="1" y="2.5" width="10" height="7" rx="1" fill="none" stroke="var(--teal)" stroke-width="1.2"/><path d="M1.5 3 L6 6.5 L10.5 3" fill="none" stroke="var(--teal)" stroke-width="1.2"/></svg>
          tessalyanimaleyecare@mailbrook.net
        </li>
        <li class="web">
          <svg viewBox="0 0 12 12" aria-hidden="true"><circle cx="6" cy="6" r="5" fill="none" stroke="var(--teal)" stroke-width="1.1"/><ellipse cx="6" cy="6" rx="2.2" ry="5" fill="none" stroke="var(--teal)" stroke-width="1"/><path d="M1 6 H11" stroke="var(--teal)" stroke-width="1"/></svg>
          <span>www.<strong>tessalyanimaleyecare</strong>.net</span>
        </li>
      </ul>
    </div>
  </section>
</body>
</html>
```